Design some Business Cards

Looking for a very creative and unique design for a business card for a marketing firm. Needs to include the following:

Logo
URL: http://www.TheVellinorGroup.com
Businesss Phone: 555-318-4706

Then it will need to be customized with individual contact info:
Name
Mobile #
E-mail

Do not include address

Logo attached

```html
<!DOCTYPE html>
<html lang="en">
<head>
<meta charset="utf-8">
<title>The Vellinor Group – Business Card</title>
<link href="https://fonts.googleapis.com/css2?family=Oswald:wght@400;500&family=Roboto+Condensed:wght@400;700&display=swap" rel="stylesheet">
<style>
  :root {
    --bg: #e4e5e6;
    --card: #ffffff;
    --blue: #2b8fd0;
    --blue-deep: #1d5f99;
    --navy: #1f5a8c;
    --ink: #4a4b4d;
    --gray-dark: #6f7072;
    --gray-mid: #9a9b9d;
    --gray-light: #d2d3d4;
  }
  * { margin: 0; padding: 0; box-sizing: border-box; }
  html, body { width: 1200px; height: 1200px; overflow: hidden; background: var(--bg); }
  .canvas { position: relative; width: 1200px; height: 1200px; }
  .card {
    position: absolute; left: 222px; width: 756px; height: 446px;
    background: var(--card); overflow: hidden;
  }
  .card--front { top: 103px; }
  .card--back { top: 630px; }
  .card svg.art { position: absolute; inset: 0; width: 756px; height: 446px; }

  .brand {
    position: absolute; left: 380px; top: 160px;
    display: flex; align-items: center; gap: 22px;
  }
  .brand__mark {
    width: 112px; height: 112px; border-radius: 50%;
    border: 6px solid var(--gray-dark);
  }
  .brand__name {
    font-family: "Roboto Condensed", sans-serif; font-weight: 700;
    font-size: 34px; line-height: 1.05; letter-spacing: 1px;
    text-transform: uppercase; color: var(--navy);
  }

  .contact { position: absolute; left: 92px; top: 40px; list-style: none; }
  .contact__item {
    display: flex; align-items: center; height: 48px;
    font-family: "Roboto Condensed", sans-serif; font-weight: 700; font-size: 21px;
  }
  .contact__item--blue { color: var(--navy); }
  .contact__item--dark { color: var(--ink); }
  .contact__icon { width: 30px; height: 30px; margin-right: 18px; flex: none; }

  .person { position: absolute; left: 120px; top: 322px; text-align: center; }
  .person__name {
    font-family: "Oswald", sans-serif; font-weight: 400; font-size: 44px;
    line-height: 1; color: var(--ink); letter-spacing: 0.5px;
  }
  .person__name span { color: var(--navy); }
  .person__role {
    font-family: "Roboto Condensed", sans-serif; font-size: 13px;
    color: var(--ink); margin-top: 10px;
  }
</style>
</head>
<body>
<div class="canvas">

  <!-- Front -->
  <section class="card card--front">
    <svg class="art" viewBox="0 0 756 446" aria-hidden="true">
      <defs>
        <radialGradient id="front-gray" cx="0.25" cy="0.55" r="0.7">
          <stop offset="0" stop-color="#f2f2f2"/>
          <stop offset="0.45" stop-color="#a9aaac"/>
          <stop offset="1" stop-color="#77787a"/>
        </radialGradient>
        <linearGradient id="front-blue" x1="0" x2="1">
          <stop offset="0" stop-color="#2f9be0"/>
          <stop offset="1" stop-color="#1b4f80"/>
        </linearGradient>
      </defs>
      <rect width="756" height="446" fill="url(#front-gray)"/>
      <rect x="0" y="94" width="420" height="51" fill="#ffffff"/>
      <rect x="0" y="145" width="420" height="49" fill="url(#front-blue)"/>
      <rect x="0" y="194" width="420" height="60" fill="#ffffff"/>
      <circle cx="780" cy="360" r="572" fill="#5d5e60"/>
      <circle cx="780" cy="360" r="562" fill="#ffffff"/>
      <path d="M575 0 Q275 110 228 446" fill="none" stroke="var(--navy)" stroke-width="9"/>
    </svg>
    <div class="brand">
      <div class="brand__mark"></div>
      <div class="brand__name">The<br>Vellinor<br>Group</div>
    </div>
  </section>

  <!-- Back -->
  <section class="card card--back">
    <svg class="art" viewBox="0 0 756 446" aria-hidden="true">
      <defs>
        <linearGradient id="back-gray" x1="0" x2="1">
          <stop offset="0" stop-color="#7b7c7e"/>
          <stop offset="1" stop-color="#a3a4a6"/>
        </linearGradient>
        <linearGradient id="back-edge" x1="0" x2="1">
          <stop offset="0" stop-color="#ffffff" stop-opacity="0"/>
          <stop offset="1" stop-color="#cfd0d1"/>
        </linearGradient>
      </defs>
      <rect width="756" height="446" fill="url(#back-gray)"/>
      <rect x="380" y="188" width="376" height="47" fill="#ffffff"/>
      <rect x="380" y="235" width="376" height="65" fill="var(--blue)"/>
      <rect x="380" y="300" width="376" height="48" fill="#ffffff"/>
      <path d="M540 300 Q520 360 470 446" fill="none" stroke="var(--navy)" stroke-width="8"/>
      <circle cx="-100" cy="230" r="660" fill="url(#back-edge)"/>
      <circle cx="-100" cy="230" r="648" fill="#ffffff"/>
      <rect x="0" y="0" width="70" height="446" fill="url(#back-edge)" opacity="0.35"/>
    </svg>

    <ul class="contact">
      <li class="contact__item contact__item--blue">
        <svg class="contact__icon" viewBox="0 0 30 30"><circle cx="15" cy="15" r="15" fill="var(--navy)"/><rect x="11" y="7" width="8" height="16" rx="2" fill="#fff"/></svg>
        Mobile:
      </li>
      <li class="contact__item contact__item--dark">
        <svg class="contact__icon" viewBox="0 0 30 30"><circle cx="15" cy="15" r="15" fill="var(--ink)"/><rect x="8" y="10" width="14" height="10" rx="1" fill="#fff"/><path d="M8 10 L15 16 L22 10" fill="none" stroke="var(--ink)" stroke-width="1.5"/></svg>
        E-mail:
      </li>
      <li class="contact__item contact__item--blue">
        <svg class="contact__icon" viewBox="0 0 30 30"><circle cx="15" cy="15" r="15" fill="var(--navy)"/><path d="M8 12 Q15 6 22 12 L20 14 L17 12 L13 12 L10 14 Z" fill="#fff"/><rect x="10" y="15" width="10" height="7" rx="1" fill="#fff"/></svg>
        Business Phone: 555-318-4706
      </li>
      <li class="contact__item contact__item--dark">
        <svg class="contact__icon" viewBox="0 0 30 30"><circle cx="15" cy="15" r="15" fill="var(--ink)"/><circle cx="15" cy="15" r="7" fill="none" stroke="#fff" stroke-width="1.6"/><path d="M8 15 H22 M15 8 V22" stroke="#fff" stroke-width="1.4"/></svg>
        Website: www.TheVellinorGroup.com
      </li>
    </ul>

    <div class="person">
      <div class="person__name">JOHN <span>DOE</span></div>
      <div class="person__role">marketing expert</div>
    </div>
  </section>

</div>
</body>
</html>
```